Mission statement design for a secondary school

We have the content of our mission statement and need an appealing layout. The design should fit on a poster or A4 page. The content grouping in the document should also be graphically recognizable. Our target group are young people and their parents as well as the school staff, which is why we need a modern design that is not out after 2 years. It must be easy to grasp visually and graphically simple.

Target Market(s)

Actors of the school

Requirements
Must have
• cantonal logo including school name see document can be integrated as a header
Should not have
• References to trademarks or third parties

```html
<!DOCTYPE html>
<html lang="de">
<head>
<meta charset="utf-8">
<title>Unser Leitbild</title>
<link href="https://fonts.googleapis.com/css2?family=Raleway:wght@700;800&family=Open+Sans:wght@400;600&display=swap" rel="stylesheet">
<style>
  :root {
    --backdrop: #073d5f;
    --paper: #ffffff;
    --red: #e1101a;
    --red-dark: #8e0a0e;
    --ink: #2e2e2e;
    --text: #333333;
    --band-grey: #5b5b5b;
    --divider: #d6d6d6;
    --photo-a: #4d6a5e;
    --photo-b: #8aa0b8;
  }
  * { margin: 0; padding: 0; box-sizing: border-box; }
  html, body { width: 1200px; height: 1000px; overflow: hidden; }
  body { background: var(--backdrop); font-family: "Open Sans", Arial, sans-serif; color: var(--text); }

  .poster {
    position: absolute; left: 298px; top: 72px; width: 607px; height: 856px;
    background: var(--paper); overflow: hidden;
    box-shadow: 0 10px 30px rgba(0,0,0,.35);
  }
  .corner-dot {
    position: absolute; left: -23px; top: -55px; width: 110px; height: 110px;
    border-radius: 50%; background: var(--red);
  }
  .title {
    position: absolute; left: 42px; top: 60px;
    font-family: "Raleway", Arial, sans-serif; font-weight: 800; font-size: 35px;
    color: var(--ink); letter-spacing: -0.3px;
  }
  .title .accent { color: var(--red); }
  .intro {
    position: absolute; left: 44px; top: 106px; width: 250px;
    font-size: 14.5px; line-height: 19px; color: var(--ink);
  }
  .stance {
    position: absolute; left: 0; top: 196px; width: 300px; height: 180px;
    background: var(--band-grey); color: #fff;
  }
  .stance-label {
    position: absolute; left: 44px; top: -10px; width: 145px; height: 34px;
    background: var(--red); font-family: "Raleway", Arial, sans-serif;
    font-weight: 800; font-size: 24px; line-height: 34px; text-align: center;
    box-shadow: 0 0 0 2px #fff inset;
  }
  .stance-heading {
    position: absolute; left: 44px; top: 38px;
    font-family: "Raleway", Arial, sans-serif; font-weight: 800; font-size: 21px;
  }
  .stance-list { position: absolute; left: 44px; top: 76px; list-style: none; font-size: 10.2px; white-space: nowrap; }
  .stance-list li { height: 22.5px; }

  .photo-frame { position: absolute; left: 0; top: 0; width: 607px; height: 420px; }

  .section-head { position: absolute; left: 40px; height: 30px; display: flex; align-items: center; }
  .section-num {
    width: 28px; height: 28px; border-radius: 50%; background: var(--red-dark);
    color: #fff; font-family: "Raleway", Arial, sans-serif; font-weight: 800;
    font-size: 14px; display: flex; align-items: center; justify-content: center;
    box-shadow: -6px 2px 0 rgba(225,16,26,.25);
  }
  .section-title {
    margin-left: 13px; font-family: "Raleway", Arial, sans-serif;
    font-weight: 800; font-size: 23px; color: var(--red);
  }
  .section-rule { position: absolute; height: 2px; background: var(--red); }

  .column { position: absolute; list-style: none; font-size: 10.2px; line-height: 14px; }
  .column li { position: relative; padding-left: 25px; }
  .column li svg { position: absolute; left: 0; top: 1px; width: 11px; height: 11px; }
  .column-divider { position: absolute; width: 1px; background: var(--divider); }

  .community {
    position: absolute; left: 0; top: 718px; width: 607px; height: 138px;
    background: linear-gradient(180deg, #e3121b 0%, #b70b12 100%); color: #fff;
  }
  .community .section-num { background: #2b2b2b; box-shadow: -6px 2px 0 rgba(255,255,255,.25); }
  .community .section-title { color: #fff; }
  .community .column { color: #fff; }
  .community .column-divider { background: rgba(0,0,0,.25); }
</style>
</head>
<body>
<main class="poster">
  <div class="corner-dot"></div>

  <h1 class="title"><span class="accent">Unser</span> Leitbild</h1>
  <p class="intro">Es gibt drei Kategorien (Lernen, Entwicklung, Gemeinschaft) und die Haltung der Schule.</p>

  <section class="stance">
    <div class="stance-label">Haltung</div>
    <h2 class="stance-heading">An unserer Schule…</h2>
    <ul class="stance-list">
      <li>… stehen die Lernenden im Mittelpunkt.</li>
      <li>… ist Integration selbstverständlich.</li>
      <li>… begegnen wir uns respektvoll und wertschätzend.</li>
      <li>… setzen wir uns für lebenslanges Lernen ein.</li>
    </ul>
  </section>

  <svg class="photo-frame" viewBox="0 0 607 420">
    <defs>
      <linearGradient id="photoFill" x1="0" y1="0" x2="1" y2="1">
        <stop offset="0" stop-color="#4d6a5e"/>
        <stop offset="1" stop-color="#8aa0b8"/>
      </linearGradient>
    </defs>
    <circle cx="490" cy="206" r="206" fill="#8e0a0e"/>
    <circle cx="494" cy="210" r="196" fill="#e1101a"/>
    <circle cx="496" cy="212" r="187" fill="url(#photoFill)" role="img" aria-label="Foto: vier lachende Jugendliche vor einer Schultafel"/>
  </svg>

  <!-- 1 Lernen -->
  <div class="section-head" style="top:393px"><span class="section-num">1</span><span class="section-title">Lernen</span></div>
  <div class="section-rule" style="left:182px; top:409px; width:224px"></div>
  <ul class="column" style="left:52px; top:437px; width:165px">
    <li><svg viewBox="0 0 12 12"><circle cx="6" cy="6" r="6" fill="#e1101a"/><path d="M3.2 6.2l1.9 1.9 3.7-3.9" stroke="#fff" stroke-width="1.6" fill="none"/></svg>Wir begleiten unsere Lernenden hin zur Selbständigkeit.</li>
    <li style="margin-top:9px"><svg viewBox="0 0 12 12"><circle cx="6" cy="6" r="6" fill="#e1101a"/><path d="M3.2 6.2l1.9 1.9 3.7-3.9" stroke="#fff" stroke-width="1.6" fill="none"/></svg>Unsere Schule bietet eine zeitgemässe Infrastruktur.</li>
    <li style="margin-top:9px"><svg viewBox="0 0 12 12"><circle cx="6" cy="6" r="6" fill="#e1101a"/><path d="M3.2 6.2l1.9 1.9 3.7-3.9" stroke="#fff" stroke-width="1.6" fill="none"/></svg>Wir ermöglichen allen Lernenden Erfolge.</li>
  </ul>
  <div class="column-divider" style="left:218px; top:436px; height:120px"></div>
  <ul class="column" style="left:233px; top:437px; width:195px">
    <li><svg viewBox="0 0 12 12"><circle cx="6" cy="6" r="6" fill="#e1101a"/><path d="M3.2 6.2l1.9 1.9 3.7-3.9" stroke="#fff" stroke-width="1.6" fill="none"/></svg>Wir unterstützen unsere Lernenden in ihrem individuellen Kompetenzerwerb.</li>
    <li style="margin-top:9px"><svg viewBox="0 0 12 12"><circle cx="6" cy="6" r="6" fill="#e1101a"/><path d="M3.2 6.2l1.9 1.9 3.7-3.9" stroke="#fff" stroke-width="1.6" fill="none"/></svg>Wir begegnen Heterogenität mit multiprofessionellen Teams.</li>
    <li style="margin-top:9px"><svg viewBox="0 0 12 12"><circle cx="6" cy="6" r="6" fill="#e1101a"/><path d="M3.2 6.2l1.9 1.9 3.7-3.9" stroke="#fff" stroke-width="1.6" fill="none"/></svg>Wir schaffen eine wertschätzende und förderliche Atmosphäre.</li>
  </ul>
  <div class="column-divider" style="left:430px; top:436px; height:120px"></div>
  <ul class="column" style="left:446px; top:437px; width:140px">
    <li><svg viewBox="0 0 12 12"><circle cx="6" cy="6" r="6" fill="#e1101a"/><path d="M3.2 6.2l1.9 1.9 3.7-3.9" stroke="#fff" stroke-width="1.6" fill="none"/></svg>Die Unterrichtsinhalte orientieren sich an aktuellen Themen.</li>
    <li style="margin-top:9px"><svg viewBox="0 0 12 12"><circle cx="6" cy="6" r="6" fill="#e1101a"/><path d="M3.2 6.2l1.9 1.9 3.7-3.9" stroke="#fff" stroke-width="1.6" fill="none"/></svg>Wir beurteilen transparent.</li>
  </ul>

  <!-- 2 Entwicklung -->
  <div class="section-head" style="top:577px"><span class="section-num">2</span><span class="section-title">Entwicklung</span></div>
  <div class="section-rule" style="left:246px; top:592px; width:322px"></div>
  <ul class="column" style="left:52px; top:620px; width:170px">
    <li><svg viewBox="0 0 12 12"><circle cx="6" cy="6" r="6" fill="#e1101a"/><path d="M3.2 6.2l1.9 1.9 3.7-3.9" stroke="#fff" stroke-width="1.6" fill="none"/></svg>Wir entwickeln unsere Schule gemeinsam.</li>
    <li style="margin-top:9px"><svg viewBox="0 0 12 12"><circle cx="6" cy="6" r="6" fill="#e1101a"/><path d="M3.2 6.2l1.9 1.9 3.7-3.9" stroke="#fff" stroke-width="1.6" fill="none"/></svg>Alle tragen Verantwortung.</li>
    <li style="margin-top:8px"><svg viewBox="0 0 12 12"><circle cx="6" cy="6" r="6" fill="#e1101a"/><path d="M3.2 6.2l1.9 1.9 3.7-3.9" stroke="#fff" stroke-width="1.6" fill="none"/></svg>Wir sind innovativ und gehen mutig unseren Weg.</li>
  </ul>
  <div class="column-divider" style="left:218px; top:616px; height:90px"></div>
  <ul class="column" style="left:233px; top:620px; width:190px">
    <li><svg viewBox="0 0 12 12"><circle cx="6" cy="6" r="6" fill="#e1101a"/><path d="M3.2 6.2l1.9 1.9 3.7-3.9" stroke="#fff" stroke-width="1.6" fill="none"/></svg>Wir setzen unsere Fähigkeiten und Kräfte gezielt ein.</li>
    <li style="margin-top:9px"><svg viewBox="0 0 12 12"><circle cx="6" cy="6" r="6" fill="#e1101a"/><path d="M3.2 6.2l1.9 1.9 3.7-3.9" stroke="#fff" stroke-width="1.6" fill="none"/></svg>Wir bilden uns kontinuierlich weiter.</li>
  </ul>
  <div class="column-divider" style="left:428px; top:616px; height:90px"></div>
  <ul class="column" style="left:446px; top:620px; width:140px">
    <li><svg viewBox="0 0 12 12"><circle cx="6" cy="6" r="6" fill="#e1101a"/><path d="M3.2 6.2l1.9 1.9 3.7-3.9" stroke="#fff" stroke-width="1.6" fill="none"/></svg>Wir lernen alle voneinander.</li>
    <li style="margin-top:9px"><svg viewBox="0 0 12 12"><circle cx="6" cy="6" r="6" fill="#e1101a"/><path d="M3.2 6.2l1.9 1.9 3.7-3.9" stroke="#fff" stroke-width="1.6" fill="none"/></svg>Wir reflektieren unser Handeln.</li>
  </ul>

  <!-- 3 Gemeinschaft -->
  <section class="community">
    <div class="section-head" style="top:10px"><span class="section-num">3</span><span class="section-title">Gemeinschaft</span></div>
    <ul class="column" style="left:52px; top:50px; width:175px">
      <li><svg viewBox="0 0 12 12"><circle cx="6" cy="6" r="6" fill="#fff"/><path d="M3.2 6.2l1.9 1.9 3.7-3.9" stroke="#c50c14" stroke-width="1.6" fill="none"/></svg>Unsere Schule achtet die Gesundheit aller.</li>
      <li style="margin-top:8px"><svg viewBox="0 0 12 12"><circle cx="6" cy="6" r="6" fill="#fff"/><path d="M3.2 6.2l1.9 1.9 3.7-3.9" stroke="#c50c14" stroke-width="1.6" fill="none"/></svg>Die Eltern sind ein Teil unserer Schulgemeinschaft und tragen Verantwortung.</li>
    </ul>
    <div class="column-divider" style="left:220px; top:44px; height:84px"></div>
    <ul class="column" style="left:233px; top:46px; width:235px">
      <li><svg viewBox="0 0 12 12"><circle cx="6" cy="6" r="6" fill="#fff"/><path d="M3.2 6.2l1.9 1.9 3.7-3.9" stroke="#c50c14" stroke-width="1.6" fill="none"/></svg>Unsere pädagogische Zusammenarbeit basiert auf einer professionellen Haltung.</li>
      <li style="margin-top:9px"><svg viewBox="0 0 12 12"><circle cx="6" cy="6" r="6" fill="#fff"/><path d="M3.2 6.2l1.9 1.9 3.7-3.9" stroke="#c50c14" stroke-width="1.6" fill="none"/></svg>Wir haben an unserer Schule Freiräume innerhalb klarer Rahmenbedingungen.</li>
    </ul>
    <div class="column-divider" style="left:464px; top:44px; height:84px"></div>
    <ul class="column" style="left:474px; top:48px; width:120px">
      <li><svg viewBox="0 0 12 12"><circle cx="6" cy="6" r="6" fill="#fff"/><path d="M3.2 6.2l1.9 1.9 3.7-3.9" stroke="#c50c14" stroke-width="1.6" fill="none"/></svg>Wir legen Wert auf eine offene Kommunikation.</li>
    </ul>
  </section>
</main>
</body>
</html>
```